Quibly Brochure

I need to create the first collateral material for the launch of my new Tech Startup called Quibly. I will need to develop a Brochure that states the description of the company and it products. I Have the Quiibly logo in PSD and a preliminary brochure in power Point

Target Market(s)

APP, Game Developers, Advertising Agencies and Brands

Requirements
Must have
• It needs to be a brochure with a contemporary look. The colors are in the PSD provided. Some images in the PPT Provided might change a bit such as the dashboard layouts. Notice that the logo there is not the official one. USE ONLY THE QUIBLY LOGO. NOT THE TRIBALES Y MORA logos.
Nice to have
• Clean design. Modern and readable fonts

```html
<!DOCTYPE html>
<html lang="es">
<head>
<meta charset="utf-8">
<title>Quibly Brochure</title>
<link rel="stylesheet" href="https://fonts.googleapis.com/css2?family=Lato:wght@300;400;700&family=Handlee&display=swap">
<style>
  :root {
    --backdrop: #e4e4e4;
    --page-dark: #272727;
    --page-dark-2: #343434;
    --orange: #f0a62a;
    --orange-deep: #e89a1e;
    --accent-red: #b8401e;
    --logo-orange: #e2703a;
    --script-cream: #fbe9d2;
    --body-light: #d9d9d9;
    --white: #ffffff;
    --rule-grey: #8a8a8a;
  }
  * { box-sizing: border-box; margin: 0; padding: 0; }
  html, body { width: 1200px; height: 823px; overflow: hidden; }
  body { background: var(--backdrop); font-family: "Lato", sans-serif; position: relative; }

  .page {
    position: absolute; top: 45px; width: 483px; height: 675px;
    background: radial-gradient(ellipse at 70% 30%, var(--page-dark-2), var(--page-dark) 70%);
    overflow: hidden;
  }
  .page--front { left: 98px; }
  .page--inside { left: 664px; }

  .top-rule { position: absolute; top: 45px; height: 10px; z-index: 2; }
  .top-rule span { display: block; height: 2px; background: var(--orange); margin-bottom: 2px; }
  .top-rule--front { left: 98px; width: 258px; }
  .top-rule--inside { left: 664px; width: 258px; }

  .script {
    font-family: "Handlee", cursive; color: var(--script-cream);
    text-shadow: 0 0 6px rgba(240, 140, 40, .9), 0 0 12px rgba(240, 120, 30, .6);
  }
  .brand-name { font-family: "Lato", sans-serif; font-weight: 300; color: var(--logo-orange); }

  /* Front page */
  .front-logo { position: absolute; left: 146px; top: 60px; width: 190px; height: 120px;
    display: flex; align-items: center; justify-content: center; }
  .front-logo .brand-name { font-size: 42px; }
  .front-headline { position: absolute; top: 183px; left: 0; width: 100%; text-align: center;
    font-size: 25px; line-height: 30px; }
  .front-device { position: absolute; left: 87px; top: 315px; width: 340px; height: 130px;
    border-radius: 26px; transform: rotate(-20deg);
    background: linear-gradient(160deg, #0d0d0d 0%, #1e1e1e 30%, #3a3a3a 55%, #151515 100%);
    box-shadow: 0 0 26px rgba(255, 220, 170, .35); }
  .front-band { position: absolute; left: 0; bottom: 0; width: 100%; height: 175px;
    background: linear-gradient(180deg, var(--orange) 0%, var(--orange-deep) 100%);
    border-top: 4px solid var(--rule-grey); padding: 8px 26px 0 50px; }
  .front-band h2 { font-weight: 400; font-size: 18px; line-height: 22px; color: var(--accent-red); }
  .front-band .lead { margin-top: 10px; font-size: 12px; line-height: 15px; color: var(--accent-red); }
  .questions { list-style: none; margin-top: 8px; }
  .questions li { position: relative; padding-left: 16px; font-size: 11px; line-height: 15px;
    color: var(--white); margin-bottom: 1px; }
  .questions li::before { content: ""; position: absolute; left: 0; top: 5px; width: 6px; height: 6px;
    background: var(--accent-red); }

  /* Inside page */
  .inside-headline { position: absolute; left: 34px; top: 30px; font-size: 22px; }
  .inside-logo { position: absolute; left: 386px; top: 15px; width: 90px; height: 72px;
    display: flex; align-items: center; justify-content: center; }
  .inside-logo .brand-name { font-size: 19px; }
  .flow-line { position: absolute; left: 0; top: 0; }
  .device { position: absolute; border-radius: 16px;
    background: linear-gradient(180deg, #111 0 12%, #e8eef5 12% 86%, #111 86%);
    box-shadow: 0 0 22px rgba(255, 230, 190, .55); }
  .device--login { left: 78px; top: 118px; width: 112px; height: 238px; }
  .device--list { left: 314px; top: 346px; width: 94px; height: 228px;
    background: linear-gradient(180deg, #111 0 12%, #f3f3f3 12% 86%, #111 86%); }
  .option { position: absolute; display: flex; align-items: center; gap: 10px; }
  .option__num { width: 28px; height: 28px; border: 1.5px solid var(--logo-orange); border-radius: 50%;
    color: var(--logo-orange); font-size: 18px; display: flex; align-items: center; justify-content: center; }
  .option__title { font-family: "Handlee", cursive; color: var(--logo-orange); font-size: 22px; }
  .option--one { left: 258px; top: 144px; }
  .option--two { left: 96px; top: 404px; }
  .option-text { position: absolute; color: var(--body-light); font-size: 13px; line-height: 24px; }
  .option-text--one { left: 266px; top: 194px; width: 190px; }
  .option-text--two { left: 98px; top: 446px; width: 190px; }
  .solution-band { position: absolute; left: 0; bottom: 0; width: 100%; height: 80px;
    background: linear-gradient(180deg, var(--orange) 0%, var(--orange-deep) 100%);
    border-top: 3px solid var(--rule-grey); display: flex; align-items: center; padding: 0 14px 0 23px; gap: 14px; }
  .solution-band h3 { font-weight: 400; font-size: 20px; color: var(--accent-red); }
  .solution-band p { font-size: 8.6px; line-height: 12px; font-weight: 700; color: var(--white); width: 340px; }
</style>
</head>
<body>
  <div class="top-rule top-rule--front"><span></span><span></span></div>
  <section class="page page--front">
    <div class="front-logo"><span class="brand-name">Quibly</span></div>
    <p class="front-headline script">Lorem Ipsum is simply dummy<br>text of the printing</p>
    <div class="front-device" role="img" aria-label="Smartphone lying at an angle showing an analytics dashboard app"></div>
    <div class="front-band">
      <h2>Plataforma para la promoción y monetización de aplicaciones móviles</h2>
      <p class="lead">Actualmente, Latinoamérica representa una oportunidad de negocios millonaria para los desarrolladores de juegos y aplicaciones móviles pero…</p>
      <ul class="questions">
        <li>Cómo asegurarse de lograr monetizar una aplicación?</li>
        <li>Cómo construir una base significativa de usuarios leales en una zona donde la gran mayoría de los teléfonos móviles usan el sistema de prepago?</li>
      </ul>
    </div>
  </section>

  <div class="top-rule top-rule--inside"><span></span><span></span></div>
  <section class="page page--inside">
    <p class="inside-headline script">Lorem Ipsum is simply dummy</p>
    <div class="inside-logo"><span class="brand-name">Quibly</span></div>
    <svg class="flow-line" width="483" height="675" viewBox="0 0 483 675" aria-hidden="true">
      <path d="M180 115 C 220 90, 275 88, 305 100" fill="none" stroke="#111" stroke-width="1.5" stroke-dasharray="5 4"/>
      <path d="M292 268 C 340 285, 360 320, 350 348" fill="none" stroke="#111" stroke-width="1.5" stroke-dasharray="5 4"/>
    </svg>
    <div class="device device--login" role="img" aria-label="Smartphone showing an app login screen"></div>
    <div class="device device--list" role="img" aria-label="Smartphone showing a contact list for inviting friends"></div>
    <div class="option option--one"><span class="option__num">1</span><span class="option__title">Opción</span></div>
    <p class="option-text option-text--one">Compra de monedas: el usuario utiliza un sistema de facturación SMS premium.</p>
    <div class="option option--two"><span class="option__num">2</span><span class="option__title">Opción</span></div>
    <p class="option-text option-text--two">Obtención de monedas a cambio de invitación a amigos: el usuario puede obtener monedas virtuales por invitar a sus amigos a descargar el juego o aplicación móvil.</p>
    <div class="solution-band">
      <h3>SOLUCIÓN</h3>
      <p>Quibly permite lograr el descubrimiento, promoción, instalación y monetización de juegos y aplicaciones móviles a través de una plataforma que integra varios modelos de descubrimiento, así como un motor de monetización y análisis avanzado. Obtención de usuarios leales y activos. Reducción de costos de adquisición de usuarios. Apoyo por un equipo de expertos en el mercado latinoamericano.</p>
    </div>
  </section>
</body>
</html>
```